we need an experienced designer to design the tube for our toothpaste

Design guidelines:
1. On the front side, our product logo (‘K7320’) should be prominent enough.
2. Our brand logo (‘trelvine’) could be small-size and it's just a trademark indeed.

Some information here for your reference:
1. The color of toothpaste cap is white.
2. We hope that the primary color in the design is blue.
3.‘F’ in ‘K7320’ stands for ‘trelvine’ and ‘fluoride’.
4. We will use aluminum-plastic composite materials to make toothpaste tubes. In addition to the design, we also hope that you can make relevant suggestions on the special requirements of printing.

At last, we hope that you could submit both 2D design and 3D visual effects.

Colors
0094D4
00A9DD
6FCCEA
C7EBF8
E9F6FB

Requirements
Must have
• as attached

```html
<!DOCTYPE html>
<html lang="en">
<head>
<meta charset="utf-8">
<title>K7320 Orthodontic Toothpaste – Tube Artwork</title>
<link rel="stylesheet" href="https://fonts.googleapis.com/css2?family=Barlow+Condensed:wght@500;600&family=Open+Sans:wght@400;600&display=swap">
<style>
  :root {
    --blue-deep: #0f4fa3;
    --blue-main: #1a66be;
    --blue-bright: #2f86d6;
    --ice: #e9f6fb;
    --white: #ffffff;
    --ink: #1456a8;
    --page: #f4f5f7;
    --crimp: #e4e6ea;
  }
  * { box-sizing: border-box; margin: 0; padding: 0; }
  html, body { width: 1200px; height: 800px; overflow: hidden; background: var(--page); }
  .canvas { position: relative; width: 1200px; height: 800px; }

  .tube {
    position: absolute; left: 90px; width: 1020px; height: 250px;
    background: var(--white); border-radius: 6px;
    box-shadow: 0 10px 28px rgba(20, 40, 80, .10);
    overflow: hidden;
  }
  .tube--front { top: 90px; }
  .tube--back { top: 460px; }

  .tube__crimp {
    position: absolute; right: 0; top: 0; bottom: 0; width: 34px;
    background: repeating-linear-gradient(90deg, var(--crimp) 0 2px, var(--white) 2px 4px);
  }

  .label {
    position: absolute; left: 0; top: 0; bottom: 0; width: 450px;
    background: linear-gradient(135deg, var(--blue-deep) 0%, var(--blue-main) 45%, var(--blue-bright) 100%);
    color: var(--white);
  }
  .label::before {
    content: ""; position: absolute; left: 34px; top: 0; bottom: 0; width: 7px; background: var(--white);
  }
  .label__glow {
    position: absolute; inset: 0 0 0 41px;
    background: radial-gradient(ellipse 70% 40% at 65% 22%, rgba(199,235,248,.55), rgba(199,235,248,0) 70%);
  }
  .label__inner { position: absolute; left: 58px; top: 0; right: 20px; bottom: 0; }

  .brand {
    position: absolute; top: 22px; left: 0;
    font: 600 20px/1 "Barlow Condensed", sans-serif; letter-spacing: .5px;
  }
  .product-mark {
    position: absolute; top: 46px; left: 0;
    font: 600 96px/1 "Barlow Condensed", sans-serif; letter-spacing: 4px;
  }
  .product-type {
    position: absolute; top: 148px; left: 0;
    font: 600 22px/1 "Barlow Condensed", sans-serif; letter-spacing: 2px;
  }
  .product-specs {
    position: absolute; top: 188px; left: 0; right: 0;
    display: flex; justify-content: space-between; padding-right: 28px;
    font: 600 19px/1 "Barlow Condensed", sans-serif; letter-spacing: .6px;
  }

  .claim {
    position: absolute; left: 500px; top: 62px; color: var(--ink);
    font: 600 20px/1.3 "Barlow Condensed", sans-serif; letter-spacing: 1px;
  }
  .claim__weight { margin-top: 10px; }

  .back-title {
    position: absolute; top: 22px; left: 0;
    font: 600 22px/1.25 "Barlow Condensed", sans-serif; letter-spacing: 1px; text-transform: uppercase;
  }
  .braces-visuals { position: absolute; top: 86px; left: 0; display: flex; gap: 10px; }
  .braces-visual {
    width: 120px; height: 64px; border: 2px solid var(--ice);
    background: linear-gradient(180deg, #f6c6c9 0%, #ffffff 45%, #e98a95 100%);
  }
  .benefits { position: absolute; top: 166px; left: 0; list-style: none;
    font: 600 15px/1.55 "Barlow Condensed", sans-serif; letter-spacing: .6px; }

  .info { position: absolute; left: 494px; top: 24px; width: 460px; color: var(--ink);
    font: 400 12px/1.4 "Open Sans", sans-serif; }
  .info h3 { font: 600 12.5px/1.3 "Open Sans", sans-serif; }
  .info p { margin-bottom: 12px; }
  .info .small { font-size: 9.5px; line-height: 1.35; }
  .info .small-head { font-size: 10px; font-weight: 600; }
</style>
</head>
<body>
<main class="canvas">

  <section class="tube tube--front" aria-label="Front of tube">
    <div class="label">
      <div class="label__glow"></div>
      <div class="label__inner">
        <div class="brand">trelvine</div>
        <div class="product-mark">K7320</div>
        <div class="product-type">ORTHODONTIC TOOTHPASTE</div>
        <div class="product-specs"><span>Fluoride 1450 ppm</span><span>Double Mint</span></div>
      </div>
    </div>
    <div class="claim">
      ENHANCED CAVITY PREVENTION<br>
      AND GUM PROTECTION<br>
      FOR USE WHEN WEARING METAL<br>
      BRACES AND CLEAR ALIGNERS
      <div class="claim__weight">NET WT. 85g</div>
    </div>
    <div class="tube__crimp"></div>
  </section>

  <section class="tube tube--back" aria-label="Back of tube">
    <div class="label">
      <div class="label__glow"></div>
      <div class="label__inner">
        <div class="back-title">Premium oral care during<br>orthodontic treatment</div>
        <div class="braces-visuals">
          <div class="braces-visual" role="img" aria-label="Illustration of teeth with clear aligners"></div>
          <div class="braces-visual" role="img" aria-label="Illustration of teeth with metal braces"></div>
        </div>
        <ol class="benefits">
          <li>1 Prevent Cavity</li>
          <li>2 Freshen Breath</li>
          <li>3 Strengthen Teeth</li>
        </ol>
      </div>
    </div>
    <div class="info">
      <h3>Directions</h3>
      <p>Apply at least one inch strip of the product onto a soft bristle toothbrush. Brush teeth thoroughly, for at least three minutes twice a day.</p>
      <div class="small-head">Ingredients:</div>
      <p class="small">Aqua, Sorbitol, Hydrated Silica, Glycerin, PEG-12, Sodium Lauryl Sulfate, Aroma, Cellulose Gum, Titanium Dioxide, Potassium Sorbate, Allantoin, Sodium Fluoride, Citric Acid, Peppermint Essence, Sodium Saccharin, CI 47005, CI 42090, Cinnamal.</p>
      <div class="small-head">Warnings:</div>
      <p class="small">Do not ingest. Keep out of reach of children under 6 years of age.</p>
    </div>
    <div class="tube__crimp"></div>
  </section>

</main>
</body>
</html>
```